Carpentry company Needs a business card design

We need a design for a Carpentry / building company, business card. Please think of designs out of the ordinary and try to make it eye catching. Our existing logo will need to be incorporated in the design. However feel free to change the colours of the logo to suit your design. I would like to see some designs with green /black and orange incorporated into it.These are not the only colours accepted and all designs that appeal will be accepted.

Please contact me should you have any questions
Thanks Marcus

Target Market(s)

General Public seeking carpentry work

Industry/Entity Type

Business

Contact Information for Business Card

- Current company logo ( colours can be changed)
-Phone number ,
- info@brantelworks.com.au
- brantelworks.com.au
-the facebook symbol

Font styles to use
Other font styles liked:
• You choose

Requirements
Must have
• Services we provide
• - Renovations
• -Deckings & Pergolas
• -Kitchens
• - Bathrooms
• - Intricate details
Nice to have
• an awesome design
Should not have
• Tools on the business card

```html
<!DOCTYPE html>
<html lang="en">
<head>
<meta charset="utf-8">
<title>Brantel Works – Business Card</title>
<link href="https://fonts.googleapis.com/css2?family=Open+Sans:wght@400;600;700;800&display=swap" rel="stylesheet">
<style>
  :root {
    --orange: #d08a2e;
    --ink: #242424;
    --card-dark: #2b2b2b;
    --mark-dark: #1d1d1d;
    --paper: #ffffff;
    --backdrop: #e6e2dc;
    --rule: #1a1a1a;
  }
  * { box-sizing: border-box; margin: 0; padding: 0; }
  html, body { width: 1200px; height: 1000px; overflow: hidden; }
  body {
    background: var(--backdrop);
    font-family: "Open Sans", Arial, sans-serif;
    color: var(--ink);
    position: relative;
  }
  .card {
    position: absolute;
    left: 265px;
    width: 665px;
    height: 397px;
    overflow: hidden;
    box-shadow: 0 6px 18px rgba(0,0,0,0.18);
  }
  .card--front { top: 73px; background: var(--paper); }
  .card--back { top: 532px; background: var(--card-dark); }

  .brand {
    position: absolute;
    left: 32px;
    top: 88px;
    display: flex;
    align-items: center;
    gap: 12px;
  }
  .brand__square { width: 22px; height: 22px; background: var(--orange); }
  .brand__name {
    font-size: 38px;
    font-weight: 800;
    letter-spacing: 1px;
    color: var(--ink);
    line-height: 1;
  }

  .services {
    position: absolute;
    right: 32px;
    top: 42px;
    list-style: none;
    text-align: right;
  }
  .services li {
    font-size: 16.5px;
    line-height: 23.6px;
    display: flex;
    justify-content: flex-end;
    align-items: center;
    gap: 8px;
  }
  .services .bullet {
    width: 10px; height: 10px;
    background: var(--ink);
    transform: rotate(45deg);
    display: inline-flex;
    align-items: center;
    justify-content: center;
  }
  .services .bullet::after {
    content: "";
    width: 4px; height: 4px;
    background: var(--orange);
  }

  .person__name {
    position: absolute;
    right: 32px;
    top: 226px;
    font-size: 22px;
    font-weight: 700;
    color: var(--orange);
  }
  .person__rule {
    position: absolute;
    left: 32px;
    right: 32px;
    top: 258px;
    height: 2px;
    background: var(--rule);
  }
  .person__role {
    position: absolute;
    right: 32px;
    top: 263px;
    font-size: 16px;
  }

  .contacts {
    position: absolute;
    left: 34px;
    top: 281px;
    list-style: none;
  }
  .contacts li {
    display: flex;
    align-items: center;
    gap: 7px;
    font-size: 16px;
    line-height: 25.5px;
  }
  .contacts svg { width: 16px; height: 16px; flex: none; }

  .footer-bands { position: absolute; left: 0; top: 363px; }
  .footer-url {
    position: absolute;
    right: 32px;
    top: 368px;
    font-size: 16.5px;
    letter-spacing: 1.2px;
    color: var(--paper);
  }

  .back__name {
    position: absolute;
    left: 0; right: 0;
    top: 150px;
    text-align: center;
    font-size: 54px;
    font-weight: 800;
    letter-spacing: 2px;
    color: var(--mark-dark);
  }
  .back__url {
    position: absolute;
    left: 0; right: 0;
    top: 346px;
    text-align: center;
    font-size: 18px;
    color: var(--paper);
  }
  .back__url .accent { color: var(--orange); }
</style>
</head>
<body>

<section class="card card--front">
  <div class="brand">
    <span class="brand__square"></span>
    <span class="brand__name">BRANTEL WORKS</span>
  </div>

  <ul class="services">
    <li>Renovations <span class="bullet"></span></li>
    <li>Deckings &amp; Pergolas <span class="bullet"></span></li>
    <li>Kitchens <span class="bullet"></span></li>
    <li>Bathrooms <span class="bullet"></span></li>
    <li>Intricate details <span class="bullet"></span></li>
  </ul>

  <p class="person__name">Marcus Hale</p>
  <div class="person__rule"></div>
  <p class="person__role">Director</p>

  <ul class="contacts">
    <li>
      <svg viewBox="0 0 16 16"><rect width="16" height="16" fill="var(--orange)"/></svg>
      brantelworks
    </li>
    <li>
      <svg viewBox="0 0 16 16"><rect width="16" height="16" fill="var(--orange)"/>
        <path d="M3 6 Q8 2 13 6 L11.5 7.5 L10 6.5 L6 6.5 L4.5 7.5 Z" fill="#fff"/>
        <rect x="4" y="8.5" width="8" height="4.5" fill="#fff"/></svg>
      000 000 0000
    </li>
    <li>
      <svg viewBox="0 0 16 16"><rect width="16" height="16" fill="var(--orange)"/>
        <rect x="3" y="4.5" width="10" height="7" fill="none" stroke="#fff" stroke-width="1.2"/>
        <path d="M3 4.5 L8 8.5 L13 4.5" fill="none" stroke="#fff" stroke-width="1.2"/></svg>
      info@brantelworks.com.au
    </li>
  </ul>

  <svg class="footer-bands" width="665" height="34" viewBox="0 0 665 34">
    <polygon points="0,17 373,17 357,34 0,34" fill="var(--orange)"/>
    <polygon points="390,0 665,0 665,34 367,34" fill="var(--ink)"/>
  </svg>
  <p class="footer-url">brantelworks.com.au</p>
</section>

<section class="card card--back">
  <p class="back__name">BRANTEL WORKS</p>
  <p class="back__url">www.<span class="accent">brantelworks</span>.com.au</p>
</section>

</body>
</html>
```